Graphic design of labels for scented candles

Following a change in our team structure, a deadline was put in place and the brief changed.
We need a beautiful label for our candles, one that sticks *all around the glass*. Must obviously include our logo as well as the description of the perfume.
The clientele is mainly female, between 35 and 65 years old, of a classic nature.
Brand values:
Feminine
Warm-joyful
Sophisticated-elegant
Eco-friendly, pet-friendly
Natural
Inspires confidence.
The idea is to have something different, the final appearance must be elegant and refined, which will be your challenge given the shape.

What we need:
- changeable colors
- small transparent elements which can be printed on a gold or silver paper background (example: logo, frame, elements, etc.)

- the logo (black or very dark gray) must be present + text "vegetable candle", then the perfume and below:
vegetable wax - handcrafted"
I am attaching a picture of our current labels to the files.
For the size I'll let you manage.
These labels can also be assigned to derived products such as room fragrances, pillow mists, etc.
The brand targets the middle class and above.
For the fonts I leave the choice to you.
Thank you and good luck to all !

Update: there is no longer a cat's head as a background shape, you have free choice.
THANKS

Target Market(s)

Women aged 35 to 65

Industry/Entity Type

Industrie du Parfum

Colors
00AB8E
00BBA5
67D7C9
C6EFE9
E9F9F6
59FF00
82FF00
B8FF75
E3FFCB
F4FFEA
FFF300
FFF600
FEFA6F
FFFEC7
FFFEE8
FFC000
F8CF3A
FAE287
FDF2CF
FEFAEE
F0912C
F2A743
F7CA91
FBE8D2
FDF5EE
EE7325
F08F49
F5BC92
FAE3D3
FDF4ED
EB3D1F
EC4F4E
F09395
F8D3D4
FCEDEE
E54698
E96AAD
F1A4CE
F9D9EA
FCEFF6
A7469A
B969AE
D3A5CF
EDDBEB
F8F0F9
6B429C
8869AF
B7A5CE
E3DAEB
F3F0F8

Requirements
Must have
• modifiable colors - small transparent elements which can be printed on a gold or silver paper background (example: frame, elements, etc.) - the logo (black or very dark gray) must be present + text "vegetable candle, then the perfume and below: vegetable wax - handcrafted"
Nice to have
• Elements that could be made transparent (logo text frame) to be able to edit on gold papers and give a luxurious appearance
Should not have
• no childish appearance.

```html
<!DOCTYPE html>
<html lang="en">
<head>
<meta charset="utf-8">
<title>Velora Vegetable Candle Label</title>
<link href="https://fonts.googleapis.com/css2?family=Montserrat:wght@400;500;600&family=Kaushan+Script&display=swap" rel="stylesheet">
<style>
  :root {
    --page-bg: #eceaee;
    --label-fill: #0b0b0b;
    --label-edge: #0f7a5a;
    --accent-green: #0d6b4f;
    --tan: #b7a78f;
    --flag-red: #d52b1e;
    --white: #ffffff;
  }
  * { margin: 0; padding: 0; box-sizing: border-box; }
  html, body {
    width: 1200px;
    height: 1200px;
    overflow: hidden;
    background: var(--page-bg);
  }
  .canvas {
    position: relative;
    width: 1200px;
    height: 1200px;
    display: flex;
    align-items: center;
    justify-content: center;
  }
  .label {
    position: relative;
    width: 1000px;
    height: 700px;
  }
  .label-shape {
    position: absolute;
    inset: 0;
    width: 100%;
    height: 100%;
  }
  .label-content {
    position: absolute;
    inset: 0;
    display: flex;
    flex-direction: column;
    align-items: center;
    font-family: "Montserrat", sans-serif;
    color: var(--tan);
  }
  .brand {
    margin-top: 150px;
    display: flex;
    align-items: center;
    gap: 14px;
  }
  .brand-dot {
    width: 18px;
    height: 18px;
    border-radius: 50%;
    background: var(--tan);
  }
  .brand-name {
    font-family: "Montserrat", sans-serif;
    font-weight: 600;
    font-size: 78px;
    line-height: 1;
    letter-spacing: 2px;
    color: var(--tan);
  }
  .rule {
    height: 3px;
    background: var(--tan);
  }
  .rule-top { width: 500px; margin-top: 14px; }
  .product-type {
    margin-top: 12px;
    font-size: 42px;
    font-weight: 500;
    letter-spacing: 1px;
    color: var(--tan);
  }
  .scent-name {
    margin-top: 10px;
    font-family: "Kaushan Script", cursive;
    font-size: 150px;
    line-height: 1.1;
    color: var(--accent-green);
    transform: skewX(-6deg);
  }
  .materials {
    margin-top: 8px;
    display: flex;
    align-items: center;
    gap: 12px;
    font-size: 27px;
    font-weight: 500;
    color: var(--tan);
  }
  .materials svg { width: 30px; height: 30px; }
  .rule-bottom { width: 520px; height: 2px; margin-top: 8px; }
  .website {
    margin-top: 8px;
    font-size: 24px;
    color: var(--tan);
  }
  .origin-flag {
    margin-top: 12px;
    width: 30px;
    height: 30px;
  }
</style>
</head>
<body>
  <main class="canvas">
    <section class="label">
      <svg class="label-shape" viewBox="0 0 1000 700" aria-hidden="true">
        <path d="M40 40 Q500 -20 960 40 Q930 200 950 340 Q990 430 930 520 Q860 600 700 640 Q580 650 500 690 Q420 650 300 640 Q140 600 70 520 Q10 430 50 340 Q70 200 40 40 Z"
              fill="var(--label-fill)" stroke="var(--label-edge)" stroke-width="8" stroke-linejoin="round"/>
      </svg>
      <div class="label-content">
        <div class="brand">
          <span class="brand-dot"></span>
          <span class="brand-name">Velora</span>
        </div>
        <div class="rule rule-top"></div>
        <p class="product-type">VEGETABLE CANDLE</p>
        <p class="scent-name">Perfume</p>
        <div class="materials">
          <svg viewBox="0 0 30 30" aria-hidden="true">
            <path d="M6 24 Q6 8 24 6 Q22 22 6 24 Z M6 24 L18 12" fill="none" stroke="var(--tan)" stroke-width="2"/>
          </svg>
          <span>VEGETABLE WAX - HANDCRAFTED</span>
          <svg viewBox="0 0 30 30" aria-hidden="true">
            <circle cx="15" cy="15" r="10" fill="none" stroke="var(--tan)" stroke-width="2"/>
            <path d="M10 15 L14 19 L21 11" fill="none" stroke="var(--tan)" stroke-width="2"/>
          </svg>
        </div>
        <div class="rule rule-bottom"></div>
        <p class="website">velora-candle.com</p>
        <svg class="origin-flag" viewBox="0 0 30 30" aria-hidden="true">
          <rect width="30" height="30" fill="var(--flag-red)"/>
          <rect x="12" y="6" width="6" height="18" fill="var(--white)"/>
          <rect x="6" y="12" width="18" height="6" fill="var(--white)"/>
        </svg>
      </div>
    </section>
  </main>
</body>
</html>
```